Vro Klinieken website for a maxillofacial surgery clinic

It's a website for a clinic for maxillofacial surgery in WordPress . The website doesn't need to be complicated but has to look professional. It needs to be in Dutch so i can give the texts. Similar websites are www.tandartsenpraktijkvelmor.nl or www.tbospecialisten.nl. Pages would be sort of similar to https://hetcentrumvoorgezichtszorg.nl/ or https://wolderveenclinics.nl/. Those lasts are maxillofacial surgery clinic websites, but there are little more extensive.
I uploaded the logo. If this is not the proper quality i can upload the eps. Logo was made through printhive.

Target Market(s)

Patients who can find me and see information about the clinic

Industry/Entity Type

Healthcare

Coding

Coded - Design and coding required

Number of Pages Required

5+ page

Font styles to use
Other font styles liked:
• Something standard professional

Colors
0054AA
0677BA
7BADD7
CADEEF
E8F1F8

Requirements
Nice to have
• Something in line with the logo. I prefer a little dark like the darker logos but I'm not sure if that's professional. Logos zbpor and gvls are instances i'm registered to so they will have to be on the website too but small somewhere.

```html
<!DOCTYPE html>
<html lang="nl">
<head>
<meta charset="utf-8">
<title>Vro Klinieken – Kaakchirurgie</title>
<link href="https://fonts.googleapis.com/css2?family=Open+Sans:wght@400;600;700&family=Poppins:wght@400;500;600&display=swap" rel="stylesheet">
<style>
:root{
  --navy:#1c2d4f;
  --navy-2:#233a5e;
  --nav-bar:#3b5577;
  --topbar:#1b3548;
  --blue:#1f9ad6;
  --blue-dark:#0054aa;
  --light:#eef3f5;
  --line:#dfe6ec;
  --text:#5a6270;
  --heading:#1f2c45;
  --white:#fff;
}
*{box-sizing:border-box;margin:0;padding:0}
html,body{width:1200px;height:5304px;overflow:hidden}
body{font-family:"Open Sans",sans-serif;color:var(--text);background:var(--white);position:relative}
.sec{position:absolute;left:0;width:1200px}
.abs{position:absolute}
.h2{font-family:"Poppins",sans-serif;font-weight:400;font-size:34px;color:var(--heading);white-space:nowrap}
.eyebrow{font-size:10px;font-weight:600;text-transform:uppercase;letter-spacing:.3px;color:#6b7482}
.rule{height:3px;width:88px;background:var(--blue)}
.btn{display:flex;align-items:center;justify-content:center;gap:10px;background:var(--blue);color:#fff;font-weight:700;font-size:15px;border-radius:2px}
.photo{border-radius:4px}
p.body{font-size:13.5px;line-height:23px}

.topbar{top:0;height:46px;background:var(--topbar);font-size:10px;color:#9fb1c0}
.header{top:46px;height:129px;background:#fff}
.logo-name{font-family:"Poppins",sans-serif;font-weight:500;font-size:26px;color:var(--blue-dark);white-space:nowrap}
.hinfo{display:flex;gap:12px;font-size:11px;white-space:nowrap}
.hinfo b{display:block;color:var(--blue-dark);font-weight:600;font-size:12px;margin-bottom:4px}
.nav{top:175px;left:78px;width:1044px;height:57px;background:var(--nav-bar);display:flex;align-items:center}
.nav a{color:#fff;font-size:11px;font-weight:700;text-decoration:none;position:absolute;top:0;height:57px;display:flex;align-items:center;transform:translateX(-50%)}
.nav .active{background:var(--blue);width:72px;justify-content:center;left:71px!important}
.hero{top:232px;height:598px;background:linear-gradient(100deg,#2b3c5d 0%,#3e5374 45%,#1e2f4f 100%)}
.hero h1{font-family:"Open Sans",sans-serif;font-weight:700;font-size:46px;line-height:54px;color:#fff;text-align:center;width:100%;top:200px}
.why{top:830px;height:498px;background:var(--light)}
.card{top:195px;width:340px;height:241px;background:#fff;box-shadow:0 2px 8px rgba(0,0,0,.08);text-align:center}
.card .num{position:absolute;right:0;top:0;width:64px;height:52px;background:var(--light);border-bottom-left-radius:40px;font-size:14px;font-weight:700;color:#444;display:flex;align-items:center;justify-content:center}
.card .ico{width:72px;height:72px;border-radius:50%;background:#e9f1f6;margin:42px auto 0;display:flex;align-items:center;justify-content:center}
.card h3{font-size:16px;font-weight:600;color:#222;margin-top:24px}
.card span{font-size:10px;font-weight:700;color:var(--blue);display:block;margin-top:10px}
.about{top:1328px;height:617px;background:#fff}
.feat{display:flex;align-items:center;gap:22px;font-size:15px;color:#333;line-height:24px}
.services{top:2000px;height:610px;background:var(--navy)}
.tabs{top:1945px;left:66px;width:1070px;height:107px;background:#fff;border-top:4px solid var(--navy);display:flex;box-shadow:0 2px 6px rgba(0,0,0,.08)}
.tab{flex:1;display:flex;align-items:center;justify-content:center;font-size:15px;font-weight:600;color:#222;border-left:1px solid var(--line);position:relative}
.tab.on{background:var(--blue);color:#fff;border:none}
.tab.on::after{content:"";position:absolute;bottom:-12px;left:50%;margin-left:-12px;border:12px solid transparent;border-bottom:0;border-top-color:var(--blue)}
.gallery{top:2610px;height:744px;background:#fff}
.steps{top:3354px;height:647px;background:var(--light)}
.step-box{left:550px;width:100px;height:100px;background:#fff;box-shadow:0 2px 8px rgba(0,0,0,.1);display:flex;align-items:center;justify-content:center}
.step-box i{position:absolute;left:-10px;top:-16px;width:30px;height:30px;border-radius:50%;background:var(--blue);color:#fff;font-style:normal;font-size:12px;font-weight:700;display:flex;align-items:center;justify-content:center;border:3px solid #fff}
.step-t{left:702px;font-size:16px;color:var(--heading);line-height:22px}
.step-p{left:702px;width:400px;font-size:12.5px;line-height:23px}
.contact{top:4001px;height:722px;background:#fff}
.form{left:591px;top:111px;width:487px;height:549px;background:#fff;border-top:4px solid var(--navy);box-shadow:0 2px 10px rgba(0,0,0,.1)}
.form label{position:absolute;font-size:13px;font-weight:600;color:#222}
.form .in{position:absolute;border:1px solid var(--line);font-size:11px;color:#9aa2ac;padding:12px 16px}
.citem{left:138px;display:flex;align-items:center;gap:22px;font-size:13px}
.cdot{width:36px;height:36px;border-radius:50%;background:#eef5fa;display:flex;align-items:center;justify-content:center}
.footer{top:4723px;height:581px;background:var(--navy);color:#dfe6ef}
.footer h4{font-family:"Poppins",sans-serif;font-weight:500;font-size:20px;color:#fff}
.links{font-size:13.5px;line-height:31px}
.links div::before{content:"›";margin-right:12px;font-weight:700}
.infobar{left:86px;top:432px;width:1025px;height:85px;background:var(--navy-2);display:flex;align-items:center;border-radius:3px}
.ib{flex:1;display:flex;align-items:center;gap:26px;padding-left:28px;font-size:14px;line-height:22px;white-space:nowrap}
.ib b{display:block;font-weight:600}
</style>
</head>
<body>

<section class="sec topbar">
  <div class="abs" style="left:78px;top:16px;display:flex;gap:40px"><span>☏ +31 10 555 0100</span><span>balie@vroklinieken.nl</span></div>
  <div class="abs" style="right:78px;top:16px">Zoek informatie</div>
</section>

<header class="sec header">
  <div class="abs" style="left:90px;top:34px;display:flex;align-items:center;gap:12px">
    <span style="width:30px;height:30px;border-radius:50%;background:var(--blue-dark)"></span>
    <span class="logo-name">Vro Klinieken</span>
  </div>
  <div class="abs hinfo" style="left:490px;top:38px">
    <svg width="32" height="28" viewBox="0 0 32 28" fill="none" stroke="#1f9ad6" stroke-width="2"><rect x="6" y="2" width="24" height="18"/><path d="M6 4l12 9 12-9"/><path d="M2 8v18h22"/></svg>
    <div><b>Email</b>info@vroklinieken.nl</div>
  </div>
  <div class="abs hinfo" style="left:750px;top:38px">
    <svg width="28" height="28" viewBox="0 0 24 24" fill="none" stroke="#1f9ad6" stroke-width="1.8"><path d="M5 3l4 1 1 5-3 2a12 12 0 0 0 6 6l2-3 5 1 1 4c-1 2-3 2-5 2A17 17 0 0 1 2 7c0-2 1-4 3-4z"/></svg>
    <div><b>Telefoon</b>(010) 555-0142</div>
  </div>
  <div class="abs hinfo" style="left:938px;top:38px">
    <svg width="22" height="28" viewBox="0 0 22 28" fill="none" stroke="#1f9ad6" stroke-width="2"><path d="M11 26S2 16 2 10a9 9 0 0 1 18 0c0 6-9 16-9 16z"/><circle cx="11" cy="10" r="3"/></svg>
    <div><b>Locatie</b>Kliniekweg 12, Rotterdam</div>
  </div>
</header>

<nav class="sec nav">
  <a class="active" style="left:35px">THUIS</a>
  <a style="left:194px">BEHANDELINGEN</a>
  <a style="left:344px">VERGOEDING</a>
  <a style="left:498px">ONS TEAM</a>
  <a style="left:651px">FOLDERS</a>
  <a style="left:830px">CONTACT</a>
</nav>

<section class="sec hero" role="img" aria-label="Tandarts in blauwe handschoenen behandelt een patiënt in de behandelkamer">
  <h1 class="abs">Smiles Transformeren,<br>Zelfvertrouwen Herstellen</h1>
  <p class="abs" style="top:325px;width:100%;text-align:center;color:#fff;font-size:13.5px;line-height:21px">Lorem ipsum dolor sit amet, consectetur adipiscing elit<br>sed do eiusmod tempor incidid</p>
  <div class="abs" style="left:539px;top:396px;width:130px;height:47px;border:2px solid #fff;color:#fff;font-size:12px;font-weight:700;display:flex;align-items:center;justify-content:center">MEER LEREN</div>
</section>

<section class="sec why">
  <div class="abs eyebrow" style="width:100%;text-align:center;top:59px">Zie het verschil</div>
  <h2 class="abs h2" style="width:100%;text-align:center;top:84px">Waarom Voor Ons Kiezen</h2>
  <div class="abs rule" style="left:556px;top:148px"></div>
  <div class="abs card" style="left:64px"><div class="num">01</div>
    <div class="ico"><svg width="34" height="34" viewBox="0 0 24 24" fill="none" stroke="#1f9ad6" stroke-width="1.4"><circle cx="12" cy="12" r="9"/><circle cx="12" cy="12" r="3"/><path d="M12 3v3M12 18v3M3 12h3M18 12h3"/></svg></div>
    <h3>Ervaring</h3><span>READ MORE</span></div>
  <div class="abs card" style="left:432px"><div class="num">02</div>
    <div class="ico"><svg width="34" height="34" viewBox="0 0 24 24" fill="none" stroke="#1f9ad6" stroke-width="1.4"><circle cx="8" cy="8" r="3"/><circle cx="16" cy="8" r="3"/><path d="M2 20c0-4 3-6 6-6s6 2 6 6M10 20c0-4 3-6 6-6s6 2 6 6"/></svg></div>
    <h3>Klantgericht</h3><span>READ MORE</span></div>
  <div class="abs card" style="left:798px"><div class="num">03</div>
    <div class="ico"><svg width="34" height="34" viewBox="0 0 24 24" fill="none" stroke="#1f9ad6" stroke-width="1.4"><path d="M4 14v-2a8 8 0 0 1 16 0v2"/><rect x="3" y="13" width="4" height="6" rx="1"/><rect x="17" y="13" width="4" height="6" rx="1"/></svg></div>
    <h3>Professioneel</h3><span>READ MORE</span></div>
</section>

<section class="sec about">
  <div class="abs" style="left:93px;top:60px;font-size:11px;font-weight:600;color:#444">Over Ons</div>
  <h2 class="abs h2" style="left:93px;top:87px;font-size:32px">Precisiechirurgie, Persoonlijke Zorg</h2>
  <div class="abs rule" style="left:93px;top:146px;width:92px"></div>
  <h3 class="abs" style="left:93px;top:178px;font-size:20px;font-weight:600;color:var(--heading)">Precisie in Beweging, Schoonheid in Elk Detaill</h3>
  <p class="abs body" style="left:93px;top:222px;width:502px">Lorem ipsum dolor sit amet, consectetur adipiscing elit, sed do eiusmod tempor incididunt ut labore et dolore magna aliqua. Ut enim ad minim veniam, quis nostrud exercitation ullamco laboris nisi ut aliquip ex ea commodo consequat. Duis aute irure dolor in reprehenderit in volup tate velit esse cillum dolore eu fugiat nulla pariatur. Excepteur sint occ aecat cupidatat non proident, sunt in culpa qui officia deserunt mollit. proident, sunt in culpa qui officia deserunt mollit.</p>
  <div class="abs feat" style="left:96px;top:420px">
    <svg width="44" height="44" viewBox="0 0 24 24" fill="none" stroke="#1f9ad6" stroke-width="1.3"><path d="M12 2l3 4 5 1-1 5 2 4-5 1-2 5-4-3-4 3-1-5-5-2 3-4-1-5 5 0z"/></svg>
    <span>Bewezen<br>Track Record</span></div>
  <div class="abs feat" style="left:372px;top:420px">
    <svg width="44" height="44" viewBox="0 0 24 24" fill="none" stroke="#1f9ad6" stroke-width="1.3"><circle cx="12" cy="6" r="3"/><path d="M4 20l4-8h8l4 8zM2 22h20"/></svg>
    <span>Persoonlijke<br>Aanpak</span></div>
  <div class="abs btn" style="left:93px;top:518px;width:154px;height:41px">Meer Leren
    <svg width="16" height="14" viewBox="0 0 16 14" fill="none" stroke="#fff" stroke-width="2"><path d="M1 7h13M9 2l5 5-5 5"/></svg></div>
  <div class="abs" style="left:669px;top:51px;width:444px;height:444px;border-radius:50%;border:2px solid #c8d6e2"></div>
  <div class="abs" role="img" aria-label="Lachend jong meisje in de tandartsstoel" style="left:685px;top:67px;width:412px;height:412px;border-radius:50%;background:linear-gradient(150deg,#7fb0d4,#dfc8b4 55%,#6b8fb0)"></div>
  <div class="abs" style="left:918px;top:295px;width:194px;height:194px;border-radius:50%;background:var(--navy);border:6px solid #fff"></div>
</section>

<section class="sec services">
  <div class="abs photo" role="img" aria-label="Glimlachende patiënte in gele trui bij de tandarts" style="left:66px;top:163px;width:521px;height:331px;background:linear-gradient(120deg,#9cc6e6,#c4a27a 55%,#7aa8cc)"></div>
  <div class="abs" style="left:617px;top:126px;font-size:10px;font-weight:700;color:var(--blue)">ONZE DIENSTEN</div>
  <h2 class="abs h2" style="left:617px;top:152px;color:#fff;font-size:36px">Symmetrie Vormgeven</h2>
  <h3 class="abs" style="left:617px;top:244px;font-size:19px;font-weight:600;color:#fff">Precisie Ambachtschap, Blijvende Transformaties</h3>
  <p class="abs body" style="left:619px;top:296px;width:505px;color:#e3e9f1">Lorem ipsum dolor sit amet, consectetur adipiscing elit, sed do eiusmo d tempor incididunt ut labore et dolore magna aliqua. Ut enim ad mini m veniam, quis nostrud exercitation ullamco laboris nisi ut aliquip ex ea commodo consequat. Duis aute irure dolor in reprehenderit in volup tate velit esse cillum dolore eu fugiat nulla pariatur. Excepteur sint occ aecat cupidatat non proident, sunt in culpa qui officia deserunt mollit. proident, sunt in culpa qui officia deserunt mollit.</p>
  <div class="abs btn" style="left:619px;top:493px;width:155px;height:45px">Meer Leren
    <svg width="16" height="14" viewBox="0 0 16 14" fill="none" stroke="#fff" stroke-width="2"><path d="M1 7h13M9 2l5 5-5 5"/></svg></div>
</section>
<div class="abs tabs">
  <div class="tab on">Kaakchirurgie</div>
  <div class="tab" style="border-left:none">Slaapgeneeskunde</div>
  <div class="tab">Plastische Chirurgie</div>
</div>

<section class="sec gallery">
  <div class="abs eyebrow" style="width:100%;text-align:center;top:30px">Onze Galerij</div>
  <h2 class="abs h2" style="width:100%;text-align:center;top:56px">Ons Recente Werk</h2>
  <div class="abs rule" style="left:556px;top:120px"></div>
  <div class="abs photo" role="img" aria-label="Tandarts steekt duim omhoog" style="left:95px;top:179px;width:232px;height:230px;background:linear-gradient(135deg,#cfe1ef,#3f7fc0)"></div>
  <div class="abs photo" role="img" aria-label="Lachende tandarts met handschoenen" style="left:354px;top:179px;width:233px;height:230px;background:linear-gradient(135deg,#e6dfd6,#5f87b8)"></div>
  <div class="abs photo" role="img" aria-label="Tandarts behandelt oudere patiënt" style="left:613px;top:179px;width:492px;height:230px;background:linear-gradient(120deg,#c9dcea,#5b7fa6 60%,#9fb8cc)"></div>
  <div class="abs photo" role="img" aria-label="Lachend meisje tijdens gebitscontrole" style="left:95px;top:434px;width:492px;height:230px;background:linear-gradient(120deg,#5d8fd6,#d6b79e 55%,#8fb3df)"></div>
  <div class="abs photo" role="img" aria-label="Tandarts met mondkapje aan het werk" style="left:613px;top:434px;width:233px;height:230px;background:linear-gradient(135deg,#b9cfdf,#3d6f9c)"></div>
  <div class="abs photo" role="img" aria-label="Meisje met tandenborstel" style="left:871px;top:434px;width:234px;height:230px;background:linear-gradient(135deg,#c9d7e0,#c9a07c)"></div>
</section>

<section class="sec steps">
  <div class="abs" role="img" aria-label="Donkerblauw vlak met vage foto van een behandelkamer" style="left:0;top:0;width:601px;height:647px;background:linear-gradient(160deg,#2b3e62,#1c2d4f)"></div>
  <div class="abs" style="left:99px;top:97px;font-size:10px;font-weight:700;color:#fff">HOE MEE TE DOEN</div>
  <h2 class="abs h2" style="left:99px;top:121px;color:#fff;font-size:30px">Stappen om in te schrijven</h2>
  <div class="abs rule" style="left:99px;top:182px"></div>
  <h3 class="abs" style="left:99px;top:230px;font-size:19px;font-weight:600;color:#fff">Gezichten Kracht Geven, Levens Verbeteren</h3>
  <p class="abs body" style="left:101px;top:282px;width:370px;color:#e3e9f1">Lorem ipsum dolor sit amet, consectetur adipiscing d tempor incididunt ut labore et dolore magna al m veniam, quis nostrud exercitation ullamco laboris commodo consequat. Duis aute irure dolor in repr tate velit esse cillum dolore eu fugiat nulla pariat aecat cupidatat</p>
  <div class="abs btn" style="left:101px;top:460px;width:154px;height:43px;font-size:14px">Contact us
    <svg width="16" height="14" viewBox="0 0 16 14" fill="none" stroke="#fff" stroke-width="2"><path d="M1 7h13M9 2l5 5-5 5"/></svg></div>

  <div class="abs step-box" style="top:108px"><i>01</i>
    <svg width="40" height="30" viewBox="0 0 40 30" fill="none" stroke="#1f9ad6" stroke-width="2.4"><rect x="2" y="2" width="36" height="26" rx="2"/><path d="M2 4l18 13L38 4"/></svg></div>
  <div class="abs step-t" style="top:110px">Kom Met Ons<br>In Contact</div>
  <p class="abs step-p" style="top:166px">Lorem ipsum dolor sit amet, consectetur adipiscing d te mpor incididunt ut labore et dolore magna alm veniam</p>

  <div class="abs step-box" style="top:278px"><i>02</i>
    <svg width="40" height="40" viewBox="0 0 24 24" fill="none" stroke="#1f9ad6" stroke-width="1.6"><rect x="3" y="3" width="6" height="5"/><rect x="14" y="7" width="6" height="5"/><circle cx="8" cy="15" r="2"/><path d="M4 22c0-3 2-4 4-4s4 1 4 4"/></svg></div>
  <div class="abs step-t" style="top:280px">Raadpleeg onze<br>experts</div>
  <p class="abs step-p" style="top:336px">Lorem ipsum dolor sit amet, consectetur adipiscing d te mpor incididunt ut labore et dolore magna alm veniam</p>

  <div class="abs step-box" style="top:447px"><i>03</i>
    <svg width="40" height="40" viewBox="0 0 24 24" fill="none" stroke="#1f9ad6" stroke-width="1.4"><circle cx="8" cy="8" r="3"/><circle cx="16" cy="8" r="3"/><path d="M2 20c0-4 3-6 6-6s6 2 6 6M10 20c0-4 3-6 6-6s6 2 6 6"/></svg></div>
  <div class="abs step-t" style="top:449px">Ontvang uw<br>behandeling</div>
  <p class="abs step-p" style="top:505px">Lorem ipsum dolor sit amet, consectetur adipiscing d te mpor incididunt ut labore et dolore magna alm veniam</p>
</section>

<section class="sec contact">
  <h2 class="abs h2" style="left:138px;top:172px;font-weight:500;line-height:48px">Kom Met Ons<br>In Contact</h2>
  <p class="abs" style="left:140px;top:286px;width:360px;font-size:12px;line-height:22px">Lorem ipsum dolor sit amet, consectetur adipiscing elit, sed do eiusmod tempor incididunt ut labore et dolore magna aliqua. Ut enim</p>
  <div class="abs" style="left:138px;top:383px;width:380px;height:1px;background:var(--line)"></div>
  <div class="abs citem" style="top:412px"><span class="cdot"><svg width="14" height="18" viewBox="0 0 22 28" fill="#1f9ad6"><path d="M11 27S2 16 2 10a9 9 0 0 1 18 0c0 6-9 17-9 17z"/></svg></span>Zorglaan 8, Rotterdam</div>
  <div class="abs citem" style="top:474px"><span class="cdot"><svg width="16" height="16" viewBox="0 0 24 24" fill="#1f9ad6"><path d="M5 3l4 1 1 5-3 2a12 12 0 0 0 6 6l2-3 5 1 1 4c-1 2-3 2-5 2A17 17 0 0 1 2 7c0-2 1-4 3-4z"/></svg></span>+31 10 555 0142</div>
  <div class="abs citem" style="top:529px"><span class="cdot"><svg width="16" height="12" viewBox="0 0 16 12" fill="#1f9ad6"><rect width="16" height="12" rx="1"/></svg></span>praktijk@vroklinieken.nl</div>

  <div class="abs form">
    <label style="left:35px;top:58px">Full Name:</label>
    <div class="in" style="left:30px;top:80px;width:424px;height:43px">Sed non neque elit</div>
    <label style="left:35px;top:161px">Email:</label>
    <div class="in" style="left:30px;top:183px;width:195px;height:43px">Sed non neque elit</div>
    <label style="left:262px;top:161px">Phone-no:</label>
    <div class="in" style="left:259px;top:183px;width:195px;height:43px">Sed non neque elit</div>
    <label style="left:35px;top:272px">Messages:</label>
    <div class="in" style="left:30px;top:294px;width:424px;height:128px">Sed non neque elit</div>
    <div class="abs btn" style="left:30px;top:451px;width:126px;height:39px;font-size:12px">SUBMIT</div>
  </div>
</section>

<footer class="sec footer">
  <div class="abs" style="left:90px;top:80px;display:flex;align-items:center;gap:10px">
    <span style="width:26px;height:26px;border-radius:50%;background:var(--blue)"></span>
    <span class="logo-name" style="color:#fff;font-size:23px">Vro Klinieken</span>
  </div>
  <div class="abs" style="left:84px;top:165px;font-size:18px;font-weight:700;color:#fff">0800-555-0190</div>
  <div class="abs" style="left:84px;top:194px;font-size:12.5px;font-weight:700;color:#fff">Call for free consultation</div>
  <p class="abs" style="left:84px;top:232px;width:280px;font-size:12px;line-height:22px">Lorem ipsum dolor sit amet, consectet sed do eiusmod tempor incididunt ut la magna aliqua. Ut enim</p>
  <div class="abs" style="left:84px;top:316px;font-size:13px;font-weight:700;color:#fff">Read more ›</div>

  <h4 class="abs" style="left:438px;top:88px">Useful Links</h4>
  <div class="abs links" style="left:445px;top:162px"><div>About Company</div><div>Leadership</div><div>Blog Post</div><div>FAQ'S</div><div>Certification</div><div>Testimonials</div></div>
  <div class="abs links" style="left:610px;top:162px"><div>Services</div><div>Industries</div><div>Feedback</div><div>Partners</div><div>Pricing</div><div>Contct</div></div>

  <h4 class="abs" style="left:788px;top:88px">Newsletter</h4>
  <p class="abs" style="left:788px;top:186px;width:320px;font-size:11.5px;font-weight:600;line-height:25px;color:#fff">Dont miss to subscribe to our news feeds, kindly fill the form below</p>
  <div class="abs" style="left:788px;top:257px;width:319px;height:47px;background:var(--navy-2);border-radius:24px 0 0 24px;font-size:12px;font-weight:600;color:#fff;padding:15px 24px">Your Email Address</div>
  <div class="abs" style="left:1054px;top:257px;width:53px;height:47px;background:var(--blue);border-radius:0 24px 24px 0;display:flex;align-items:center;justify-content:center">
    <svg width="12" height="18" viewBox="0 0 12 18" fill="none" stroke="#fff" stroke-width="2.5"><path d="M2 2l7 7-7 7"/></svg></div>

  <div class="abs infobar">
    <div class="ib"><svg width="30" height="34" viewBox="0 0 22 28" fill="none" stroke="#1f9ad6" stroke-width="1.8"><path d="M11 26S2 16 2 10a9 9 0 0 1 18 0c0 6-9 16-9 16z"/><circle cx="11" cy="10" r="3"/></svg><div><b>Location</b>Havenstraat 24, 3011 AB</div></div>
    <div class="ib"><svg width="32" height="30" viewBox="0 0 24 22" fill="none" stroke="#1f9ad6" stroke-width="1.6"><rect x="2" y="2" width="20" height="15" rx="1"/><path d="M6 7h12M6 11h8M6 17v4l4-4"/></svg><div><b>Mail us</b>support@vroklinieken.nl</div></div>
    <div class="ib"><svg width="30" height="30" viewBox="0 0 24 24" fill="none" stroke="#1f9ad6" stroke-width="1.6"><path d="M22 2L2 10l8 3 3 8z"/><path d="M10 13L22 2"/></svg><div><b>Office hrs</b>9.00am to 7.00pm (Mon-Sat)</div></div>
  </div>
  <div class="abs" style="left:86px;top:540px;font-size:11px">Vro Klinieken</div>
  <div class="abs" style="left:800px;top:540px;font-size:11px;display:flex;gap:26px"><span>Privacy Policy</span><span>Terms &amp; Conditions</span><span>Site Map</span></div>
  <div class="abs" style="left:1126px;top:488px;width:47px;height:47px;background:var(--blue);display:flex;align-items:center;justify-content:center">
    <svg width="18" height="12" viewBox="0 0 18 12" fill="none" stroke="#fff" stroke-width="2.5"><path d="M2 10l7-7 7 7"/></svg></div>
</footer>

</body>
</html>
```